Professional Business Card for Commercial Cleaning Company

We need a business card that represents our commercial janitorial cleaning company and represent several brands for our company so we do not want to highlight the logo too much. We want something that says we are professional.
Notes:No website or address as we have many locations and many websites and companies under our corporate name of "Brightvale Holdings, LLC" . Every time we hand a customer a business card they have contacted us via another brand we own but we don't want to have 21 business cards so we want to not focus on Brightvale Holdings, LLC too much since people will automatically ask "What is Brightvale Holdings, LLC" Example: Noodle Barn and Wrap Lantern restaurants are owned by "Zest! Brands" is the corporation name. Same principle here. Except we do not advertise at this time that all of our brands are connected. Hope this helps.
Target Market(s)
Commercial Cleaning
Industry/Entity Type
Janitorial Service
Contact Information for Business Card
Milo Jarvis
Business Development
555-382-9047
sales@brightvaleholdingsllc.example
Requirements
Must have
- Logo with contact information, need to be able to easily edit contact info for others in my office.
Nice to have
- Professional Image. Like to see a colorful bold look and a more standard business card look.
Should not have
- Any type of cleaning icons, tools, people or water.

```html
<!DOCTYPE html>
<html lang="en">
<head>
<meta charset="UTF-8">
<title>Brightvale Holdings, LLC — Business Card</title>
<link rel="stylesheet" href="https://fonts.googleapis.com/css2?family=Source+Sans+3:wght@400;600;700&display=swap">
<style>
  :root {
    --navy: #172c66;
    --green: #4e9a2e;
    --white: #ffffff;
    --ink-grey: #555a63;
    --page: #e6e7e9;
    --card-w: 540px;
    --card-h: 309px;
  }
  * { margin: 0; padding: 0; box-sizing: border-box; }
  html, body {
    width: 1200px;
    height: 857px;
    overflow: hidden;
    background: var(--page);
    font-family: "Source Sans 3", "Segoe UI", sans-serif;
  }
  .sheet {
    width: 1200px;
    height: 857px;
    display: flex;
    align-items: center;
    justify-content: center;
    gap: 50px;
  }
  .card {
    position: relative;
    width: var(--card-w);
    height: var(--card-h);
    overflow: hidden;
    box-shadow: 0 6px 18px rgba(0,0,0,0.18);
  }
  .card--front {
    background: var(--navy);
    display: flex;
    align-items: center;
    justify-content: center;
  }
  .wordmark {
    font-weight: 700;
    letter-spacing: -0.3px;
    white-space: nowrap;
  }
  .card--front .wordmark {
    color: var(--white);
    font-size: 36px;
  }
  .card-back-shape {
    position: absolute;
    inset: 0;
    width: 100%;
    height: 100%;
  }
  .contact-block {
    position: absolute;
    right: 38px;
    top: 92px;
    text-align: right;
  }
  .contact-block .wordmark {
    color: var(--navy);
    font-size: 25px;
    margin-bottom: 16px;
  }
  .person-name {
    color: var(--navy);
    font-size: 21px;
    font-weight: 600;
    line-height: 1.1;
  }
  .person-title {
    color: var(--ink-grey);
    font-size: 12.5px;
    margin-top: 2px;
  }
  .contact-lines {
    margin-top: 18px;
    list-style: none;
  }
  .contact-line {
    display: flex;
    justify-content: flex-end;
    align-items: center;
    gap: 7px;
    color: var(--ink-grey);
    font-size: 12.5px;
    line-height: 1.55;
  }
  .contact-icon {
    width: 11px;
    height: 11px;
    flex: none;
  }
</style>
</head>
<body>
<main class="sheet">
  <section class="card card--front" aria-label="Card front">
    <span class="wordmark">Brightvale Holdings, LLC</span>
  </section>

  <section class="card card--back" aria-label="Card back">
    <svg class="card-back-shape" viewBox="0 0 540 309" preserveAspectRatio="none" aria-hidden="true">
      <rect width="540" height="309" fill="var(--navy)"/>
      <ellipse cx="350" cy="240" rx="270" ry="238" fill="var(--white)"/>
      <ellipse cx="350" cy="240" rx="262" ry="230" fill="var(--green)"/>
      <ellipse cx="350" cy="240" rx="254" ry="222" fill="var(--white)"/>
    </svg>

    <div class="contact-block">
      <div class="wordmark">Brightvale Holdings, LLC</div>
      <div class="person-name">Milo Jarvis</div>
      <div class="person-title">Business Development</div>
      <ul class="contact-lines">
        <li class="contact-line">
          <span>555-382-9047</span>
          <svg class="contact-icon" viewBox="0 0 24 24" aria-hidden="true">
            <path fill="var(--green)" d="M6.6 10.8c1.4 2.8 3.8 5.1 6.6 6.6l2.2-2.2c.3-.3.7-.4 1-.2 1.1.4 2.3.6 3.6.6.6 0 1 .4 1 1V20c0 .6-.4 1-1 1C10.6 21 3 13.4 3 4c0-.6.4-1 1-1h3.5c.6 0 1 .4 1 1 0 1.3.2 2.5.6 3.6.1.3 0 .7-.2 1l-2.3 2.2z"/>
          </svg>
        </li>
        <li class="contact-line">
          <span>sales@brightvaleholdingsllc.example</span>
          <svg class="contact-icon" viewBox="0 0 24 24" aria-hidden="true">
            <rect x="2.5" y="5" width="19" height="14" fill="none" stroke="var(--green)" stroke-width="2.2"/>
            <path d="M3 6l9 7 9-7" fill="none" stroke="var(--green)" stroke-width="2.2"/>
          </svg>
        </li>
      </ul>
    </div>
  </section>
</main>
</body>
</html>
```